Need a Wordpress website for my HVAC company

I need a Wordpress website created for an HVAC company in a competitive market.
Following are some websites I like:
My current website is www.brovikclimate.com - we also have a facebook page with some pictures

We are an airconditioning and heating company that does both residential and commmercial work.
We need the following info on our website:
-mobile friendly
-Schedule an appt -repair/maintnenace/installation (i would like this option to always be on the page even if they scroll down.)
-24 hour service
-coupons /promotions
-financing
-reviews/testimonials
-about
-blog
-Our service area
The following are services we provide:
-Air conditioning - Installation/Service/Maintenance/new construction
-Heating - Installation/Service/Maintenance/new construction ( gas furnace, 2 stage furnace, electric heat)
-Duct - Repair/Replacement/Istallation - (zone systems)
-thermostats (wifi)
-Heat pump
-Air handler
-self communicating systems
-carbon monoxide testing
-hail damage
-duct sealing
-insulation
-Air cleaners - UV Air purifiers
-humidifiers

I would also like Yoast SEO add on

Target Market(s)

Anyone who needs our services HVAC contractor

Industry/Entity Type

Hvac

Contact Information for Business Card

Phone:480-555-2946
website:www.brovikclimate.com
email pmarsh@brovikclimate.com

Coding

Coded - Design and coding required

Number of Pages Required

5+ page

Font styles to use
Serif
Sans Serif

Requirements
Must have
• I wrote in brief. I already have Webb Otter. Long story I paid for 3 years already. I need someone to put website there. Ive never used Wordpress but would like a template page so I can easily add services.
Nice to have
• Clean, bright, original

```html
<!DOCTYPE html>
<html lang="en">
<head>
<meta charset="utf-8">
<title>Brovik Climate Services — Heating &amp; Cooling</title>
<link rel="stylesheet" href="https://fonts.googleapis.com/css2?family=Roboto+Condensed:wght@400;700&family=Nothing+You+Could+Do&display=swap">
<style>
  :root{
    --blue:#1a7fcf;
    --blue-deep:#1463a8;
    --red:#d9262b;
    --green:#2e9c3c;
    --navy:#1d4f9c;
    --hero-grey:#c6c4c0;
    --hero-light:#d9d7d3;
    --text-grey:#6b6b6b;
    --icon-grey:#8a8a8a;
    --slate:#49525a;
    --white:#ffffff;
  }
  *{box-sizing:border-box;margin:0;padding:0}
  html,body{width:1200px;height:676px;overflow:hidden;background:var(--white)}
  body{font-family:"Roboto Condensed",Arial,sans-serif}
  .page{position:relative;width:1200px;height:676px;overflow:hidden;background:var(--white)}

  /* utility bar */
  .utility{position:absolute;top:14px;left:0;right:0;height:22px}
  .utility > *{position:absolute;top:0;height:20px;display:flex;align-items:center}
  .phone{left:528px;color:var(--text-grey);font-size:14px;gap:4px}
  .tag{font-size:13px;font-weight:700;color:var(--white);padding:0 7px;border-radius:4px}
  .tag--repair{left:672px;background:var(--red)}
  .tag--maintenance{left:754px;background:var(--green)}
  .tag--installation{left:878px;background:var(--navy)}
  .social{width:10px;height:10px;top:5px;border-radius:50%;background:var(--icon-grey)}
  .social--one{left:1000px}
  .social--two{left:1032px}
  .search{left:1066px}

  /* navigation */
  .nav-stub{position:absolute;left:0;top:30px;width:50px;height:62px;background:var(--blue)}
  .nav{position:absolute;left:326px;top:38px;right:0;height:64px;background:var(--blue)}
  .nav a{position:absolute;top:22px;color:var(--white);text-decoration:none;font-weight:700;font-size:16px;letter-spacing:.1px}
  .nav a:nth-child(1){left:140px}
  .nav a:nth-child(2){left:220px}
  .nav a:nth-child(3){left:328px}
  .nav a:nth-child(4){left:466px}
  .nav a:nth-child(5){left:538px}
  .nav a:nth-child(6){left:675px}

  .brand{position:absolute;left:52px;top:0;width:280px;height:122px;background:var(--white);
    border-radius:0 0 6px 6px;box-shadow:0 2px 6px rgba(0,0,0,.15);
    display:flex;align-items:center;justify-content:center;gap:10px}
  .brand__mark{width:18px;height:18px;border-radius:50%;background:var(--blue)}
  .brand__name{font-weight:700;font-size:25px;color:var(--blue-deep);line-height:1.05}

  /* hero */
  .hero{position:absolute;left:0;right:0;top:102px;height:440px;
    background:linear-gradient(115deg,var(--hero-grey) 0 46%,var(--hero-light) 46% 100%)}
  .hero__title{position:absolute;left:74px;top:74px;font-family:"Nothing You Could Do",cursive;
    color:var(--white);font-size:50px;line-height:58px;font-weight:400}
  .hero__lead{position:absolute;left:80px;top:192px;width:440px;color:var(--white);font-size:20px;line-height:24px}
  .hero__call{position:absolute;left:88px;top:272px;width:130px;height:31px;background:var(--white);
    border-radius:3px;color:var(--blue);font-size:11px;font-weight:700;display:flex;align-items:center;justify-content:center}
  .hero__mascot{position:absolute;left:740px;top:8px;width:220px;height:330px;border-radius:12px;
    background:radial-gradient(ellipse at 50% 45%,#4d86c0 0%,#6f95bb 45%,rgba(217,215,211,0) 75%)}

  /* service cards */
  .card{position:absolute;top:471px;height:150px}
  .card--residential{left:86px;width:348px}
  .card--commercial{left:457px;width:337px}
  .card--energy{left:801px;width:334px}
  .card__photo{position:absolute;left:0;top:0;right:0;height:128px}
  .card--residential .card__photo{background:linear-gradient(100deg,#5a5b3d,#9a9a8f 45%,#cfd1cf)}
  .card--commercial .card__photo{background:linear-gradient(180deg,#5d9ad6,#c9d6df 55%,#a9a49b)}
  .card--energy .card__photo{background:linear-gradient(180deg,#9cc1dd,#4f5f50 50%,#6b4a36)}
  .card__label{position:absolute;left:24px;right:8px;top:103px;height:46px;
    background:linear-gradient(180deg,var(--blue),var(--blue-deep));
    color:var(--white);font-size:17px;display:flex;align-items:center;justify-content:center;letter-spacing:.3px;
    box-shadow:0 3px 6px rgba(0,0,0,.25)}
  .card__icon{position:absolute;top:-20px;width:42px;height:42px;border-radius:50%;background:var(--blue);
    border:2px solid var(--white);display:flex;align-items:center;justify-content:center}
  .card--residential .card__icon{left:150px}
  .card--commercial .card__icon{left:145px}
  .card--energy .card__icon{left:155px}

  .footer-bar{position:absolute;left:0;right:0;bottom:0;height:30px;display:flex}
  .footer-bar__progress{width:642px;background:var(--blue)}
  .footer-bar__rest{flex:1;background:var(--slate)}
</style>
</head>
<body>
<div class="page">

  <header>
    <div class="utility">
      <span class="phone">
        <svg width="11" height="11" viewBox="0 0 24 24"><path fill="#6b6b6b" d="M6.6 10.8a15 15 0 0 0 6.6 6.6l2.2-2.2c.3-.3.7-.4 1-.2 1.1.4 2.3.6 3.6.6.6 0 1 .4 1 1V20c0 .6-.4 1-1 1A17 17 0 0 1 3 4c0-.6.4-1 1-1h3.5c.6 0 1 .4 1 1 0 1.3.2 2.5.6 3.6.1.3 0 .7-.2 1z"/></svg>
        +1 800 555 0142
      </span>
      <span class="tag tag--repair">REPAIR</span>
      <span class="tag tag--maintenance">MAINTNENACE</span>
      <span class="tag tag--installation">INSTALLATION</span>
      <span class="social social--one" aria-label="Social profile"></span>
      <span class="social social--two" aria-label="Social profile"></span>
      <span class="search"><svg width="13" height="13" viewBox="0 0 24 24"><circle cx="10" cy="10" r="6.5" fill="none" stroke="#7a7a7a" stroke-width="3"/><path d="M15 15l6 6" stroke="#7a7a7a" stroke-width="3" stroke-linecap="round"/></svg></span>
    </div>
    <div class="nav-stub"></div>
    <nav class="nav">
      <a href="#">HOME</a><a href="#">ABOUT US</a><a href="#">OUR SERVICES</a><a href="#">BLOG</a><a href="#">TESTIMONIALS</a><a href="#">CONTACT US</a>
    </nav>
    <div class="brand">
      <span class="brand__mark"></span>
      <span class="brand__name">Brovik Climate<br>Services</span>
    </div>
  </header>

  <section class="hero">
    <h1 class="hero__title">High<br>Standards</h1>
    <p class="hero__lead">Our Success is not Only Due to the Quality of Our Work. It's Down to Attitude, Our Approach and the Way We Treat Our Clients</p>
    <a class="hero__call">CALL (480) 555-2946</a>
    <div class="hero__mascot" role="img" aria-label="Cartoon technician in blue uniform holding a thermometer and giving a thumbs up"></div>
  </section>

  <section class="services">
    <article class="card card--residential">
      <div class="card__photo" role="img" aria-label="Outdoor air conditioning unit beside a white house"></div>
      <div class="card__label">RESIDENTIAL</div>
      <span class="card__icon"><svg width="20" height="20" viewBox="0 0 24 24"><path d="M3 11l9-7 9 7v10h-6v-6H9v6H3z" fill="none" stroke="#fff" stroke-width="2" stroke-linejoin="round"/></svg></span>
    </article>
    <article class="card card--commercial">
      <div class="card__photo" role="img" aria-label="Rooftop commercial HVAC units under blue sky"></div>
      <div class="card__label">COMMERCIAL</div>
      <span class="card__icon"><svg width="20" height="20" viewBox="0 0 24 24"><rect x="3" y="6" width="8" height="15" fill="none" stroke="#fff" stroke-width="2"/><rect x="13" y="3" width="8" height="18" fill="none" stroke="#fff" stroke-width="2"/><path d="M6 10h2M6 14h2M16 8h2M16 12h2M16 16h2" stroke="#fff" stroke-width="2"/></svg></span>
    </article>
    <article class="card card--energy">
      <div class="card__photo" role="img" aria-label="House with solar panels on its roof"></div>
      <div class="card__label">ENERGY</div>
      <span class="card__icon"><svg width="20" height="20" viewBox="0 0 24 24"><path d="M12 3a6 6 0 0 0-3.5 10.9V17h7v-3.1A6 6 0 0 0 12 3zM9.5 20h5" fill="none" stroke="#fff" stroke-width="2" stroke-linecap="round"/></svg></span>
    </article>
  </section>

  <div class="footer-bar"><span class="footer-bar__progress"></span><span class="footer-bar__rest"></span></div>
</div>
</body>
</html>
```